Business Cards

I'd like help creating business cards with the full logo "Veltrona Capital Partners" on the back of the card (navy background with white writing), and abbreviated logo "VCP" on the front. Would like to list name, title, phone number, email, and website listed on front of card. Would like to keep very simple. Front font Arial or similar.

```html
<!DOCTYPE html>
<html lang="en">
<head>
<meta charset="utf-8">
<title>Veltrona Capital Partners — Business Cards</title>
<link href="https://fonts.googleapis.com/css2?family=Arimo:wght@400;700&display=swap" rel="stylesheet">
<style>
  :root {
    --navy: #254a7e;
    --navy-deep: #1f4274;
    --paper: #ffffff;
    --backdrop: #d9d9d7;
    --ink-light: #ffffff;
  }
  * { box-sizing: border-box; margin: 0; padding: 0; }
  html, body {
    width: 1200px; height: 801px; overflow: hidden;
    background: var(--backdrop);
    font-family: "Arimo", Arial, sans-serif;
  }
  .canvas {
    position: relative; width: 1200px; height: 801px;
    display: flex; align-items: center; justify-content: center; gap: 40px;
  }
  .card {
    width: 540px; height: 309px; position: relative; overflow: hidden;
    box-shadow: 0 6px 18px rgba(0,0,0,0.18);
  }
  /* Front */
  .card-front { background: var(--paper); }
  .front-mark {
    position: absolute; left: 44px; top: 52px;
    display: flex; align-items: center; gap: 14px;
    color: var(--navy); font-weight: 700; font-size: 52px; letter-spacing: 1px;
  }
  .front-mark .mark-square { width: 18px; height: 18px; background: var(--navy); }
  .front-band {
    position: absolute; left: 0; right: 0; bottom: 0; height: 140px;
    background: var(--navy);
    display: flex; justify-content: space-between; align-items: center;
    padding: 0 34px 0 44px; color: var(--ink-light);
  }
  .holder-name { font-weight: 700; font-size: 20px; letter-spacing: 0.5px; }
  .holder-title { font-size: 14px; margin-top: 4px; }
  .contact-list { list-style: none; font-size: 13px; line-height: 1.55; }
  .contact-list li { display: flex; align-items: center; gap: 8px; }
  .contact-list svg { width: 11px; height: 11px; flex: none; }
  /* Back */
  .card-back {
    background: var(--navy-deep);
    display: flex; flex-direction: column; align-items: center; justify-content: center;
    color: var(--ink-light); font-weight: 700;
  }
  .back-wordmark { display: flex; align-items: center; gap: 14px; font-size: 50px; letter-spacing: 2px; }
  .back-wordmark .mark-square { width: 16px; height: 16px; background: var(--ink-light); }
  .back-tagline { font-size: 17px; letter-spacing: 7px; margin-top: 10px; }
</style>
</head>
<body>
<main class="canvas">
  <section class="card card-front" aria-label="Business card front">
    <div class="front-mark"><span class="mark-square"></span><span>VCP</span></div>
    <div class="front-band">
      <div class="holder">
        <div class="holder-name">MILES HARMON</div>
        <div class="holder-title">President &amp; CEO</div>
      </div>
      <ul class="contact-list">
        <li>
          <svg viewBox="0 0 12 12"><path d="M3 1 L5 3.5 L4 5 Q5 7 7 8 L8.5 7 L11 9 L9.5 11 Q4 10 1 2.5 Z" fill="currentColor"/></svg>
          (123) 123 1234
        </li>
        <li>
          <svg viewBox="0 0 12 12"><rect x="0.5" y="2" width="11" height="8" fill="currentColor"/><path d="M0.5 2 L6 6.5 L11.5 2" fill="none" stroke="#254a7e" stroke-width="1"/></svg>
          info@yourwebsite.com
        </li>
        <li>
          <svg viewBox="0 0 12 12"><circle cx="6" cy="6" r="5.2" fill="currentColor"/><path d="M0.8 6 H11.2 M6 0.8 V11.2 M6 0.8 Q2.5 6 6 11.2 M6 0.8 Q9.5 6 6 11.2" fill="none" stroke="#254a7e" stroke-width="0.8"/></svg>
          www.yourwebsite.com
        </li>
      </ul>
    </div>
  </section>

  <section class="card card-back" aria-label="Business card back">
    <div class="back-wordmark"><span class="mark-square"></span><span>VELTRONA</span></div>
    <div class="back-tagline">CAPITAL PARTNERS</div>
  </section>
</main>
</body>
</html>
```